Vantrell OBGYN Partners LLC
...connect the dots (docs!)
Vantrell OBGYN Partners LLC -
Creative Brief
Simple
Dr. Marlene Fostwick-Abara MD FACOG
2846 Quillan Avenue Suite 240 Tucker, Ga 30091
marlene@vantrellobgynpartners.example
www.vantrellobgynpartners.example
Desire same logo continued with above second line listed as in Hire-a-medic logo by KARBIMOSS design#12 with above adjustment in subtitle
Vantrell OBGYN Partners Locum tenens option for OBGYN's ...connect to us and we will help you connect the dots in your day!

```html
<!DOCTYPE html>
<html lang="en">
<head>
<meta charset="utf-8">
<title>Vantrell OBGYN Partners – Business Card</title>
<link href="https://fonts.googleapis.com/css2?family=Open+Sans:wght@300;400&display=swap" rel="stylesheet">
<style>
  :root {
    --stage: #2e2e2e;
    --card: #ffffff;
    --cyan: #2bb6c6;
    --cyan-dark: #1f97a8;
    --pink: #e0197d;
    --ink: #4a4a4a;
    --ink-soft: #777777;
  }
  * { margin: 0; padding: 0; box-sizing: border-box; }
  html, body {
    width: 1200px; height: 1039px; overflow: hidden;
    background: var(--stage);
    font-family: "Open Sans", Arial, sans-serif;
    font-weight: 300;
  }
  .card {
    position: absolute;
    width: 750px; height: 460px;
    background: var(--card);
    border-radius: 26px;
    overflow: hidden;
    box-shadow: 0 10px 24px rgba(0,0,0,.35);
  }
  .card--front { left: 240px; top: 30px; }
  .card--back  { left: 210px; top: 545px; }

  .card__rule {
    position: absolute; left: 0; right: 0; height: 3px;
    background: var(--pink);
  }
  .card__band {
    position: absolute; left: 0; right: 0; bottom: 0;
    background: linear-gradient(180deg, var(--cyan) 0%, var(--cyan-dark) 100%);
  }

  .brand-dot {
    display: block; width: 54px; height: 54px; border-radius: 50%;
    background: var(--pink);
  }
  .brand-name {
    color: var(--cyan); font-weight: 400; letter-spacing: -0.5px; white-space: nowrap;
  }
  .tagline { color: var(--ink); white-space: nowrap; }

  /* Front */
  .front-brand {
    position: absolute; left: 0; right: 0; top: 60px;
    display: flex; flex-direction: column; align-items: center;
  }
  .front-brand .brand-name { font-size: 36px; margin-top: 58px; line-height: 1; }
  .front-brand .tagline { font-size: 27px; line-height: 1.2; }
  .front-note {
    position: absolute; left: 40px; top: 310px;
    font-size: 16px; line-height: 1.35; color: var(--ink);
  }
  .card--front .card__rule { top: 392px; }
  .card--front .card__band { height: 56px; }

  /* Back */
  .back-brand {
    position: absolute; left: 30px; top: 95px; width: 320px;
    display: flex; flex-direction: column; align-items: center;
  }
  .back-brand .brand-dot { width: 46px; height: 46px; }
  .back-brand .brand-name { font-size: 23px; margin-top: 40px; line-height: 1; }
  .back-brand .tagline { font-size: 18px; line-height: 1.25; }

  .contact { position: absolute; left: 375px; top: 50px; width: 345px; }
  .contact__company { font-size: 23px; font-weight: 400; color: var(--cyan); line-height: 1.2; letter-spacing: -0.3px; white-space: nowrap; }
  .contact__person { font-size: 15px; color: var(--ink-soft); margin-top: 4px; padding-bottom: 10px; border-bottom: 1px solid #dcdcdc; white-space: nowrap; }
  .contact__address { font-size: 16px; color: var(--ink); line-height: 1.35; margin-top: 22px; }
  .contact__lines { list-style: none; margin-top: 14px; font-size: 16px; color: var(--ink); line-height: 1.35; }
  .contact__lines li { white-space: nowrap; }
  .contact__label { color: var(--pink); display: inline-block; width: 16px; }

  .card--back .card__rule { top: 370px; }
  .card--back .card__band {
    height: 84px;
    display: flex; align-items: center; justify-content: center;
    color: #ffffff; font-size: 20px; font-weight: 400;
  }
</style>
</head>
<body>

<section class="card card--front" aria-label="Card front">
  <div class="front-brand">
    <span class="brand-dot" aria-hidden="true"></span>
    <div class="brand-name">Vantrell OBGYN Partners LLC</div>
    <div class="tagline">Connect the dots ( docs)</div>
  </div>
  <p class="front-note">
    Vantrell OBGYN Partners<br>
    Locum tenens option for OBGYN's<br>
    ...connect to us and we will help you connect the dots in your day!
  </p>
  <div class="card__rule"></div>
  <div class="card__band"></div>
</section>

<section class="card card--back" aria-label="Card back">
  <div class="back-brand">
    <span class="brand-dot" aria-hidden="true"></span>
    <div class="brand-name">Vantrell OBGYN Partners LLC</div>
    <div class="tagline">Connect the dots ( docs)</div>
  </div>
  <div class="contact">
    <div class="contact__company">Vantrell OBGYN Partners LLC</div>
    <div class="contact__person">Dr. Marlene Fostwick-Abara MD FACOG</div>
    <p class="contact__address">2846 Quillan Avenue<br>Suite 240 Tucker, Ga 30091</p>
    <ul class="contact__lines">
      <li><span class="contact__label">p</span>800.555.0147</li>
      <li><span class="contact__label">f</span>888.555.0182</li>
      <li><span class="contact__label">e</span>marlene@vantrellobgynpartners.example</li>
    </ul>
  </div>
  <div class="card__rule"></div>
  <div class="card__band">www.vantrellobgynpartners.example</div>
</section>

</body>
</html>
```